Business Card Design Project

Business Card
We are rebranding with a new logo
Industry/Entity Type
Business
Contact Information for Business Card
Dennis Marlow +61 427581962 dennis@qovo.com.au P.O. Box 872 Kelvindale QLD 4309
Requirements
Must have
- Logo

```html
<!DOCTYPE html>
<html lang="en">
<head>
<meta charset="utf-8">
<title>Qovo International – Business Card</title>
<link rel="stylesheet" href="https://fonts.googleapis.com/css2?family=Arimo:wght@400;700&display=swap">
<style>
  :root {
    --page-bg: #2a2a2c;
    --card-white: #ffffff;
    --brand-orange: #f28121;
    --brand-blue: #1b6a94;
    --text-light: #ffffff;
  }
  * { margin: 0; padding: 0; box-sizing: border-box; }
  html, body {
    width: 1200px;
    height: 1200px;
    overflow: hidden;
    background: var(--page-bg);
    font-family: "Arimo", Arial, sans-serif;
  }
  .stage {
    width: 1200px;
    height: 1200px;
    display: flex;
    align-items: center;
    justify-content: center;
  }
  .business-card {
    position: relative;
    width: 1000px;
    height: 572px;
    background: var(--card-white);
    overflow: hidden;
    box-shadow: 0 10px 30px rgba(0,0,0,0.35);
  }
  .card-wave {
    position: absolute;
    inset: 0;
    width: 100%;
    height: 100%;
  }
  .wave-fill { fill: var(--brand-orange); }
  .wave-line { fill: none; stroke: var(--brand-blue); stroke-width: 7; }
  .brand {
    position: absolute;
    left: 330px;
    top: 70px;
    width: 300px;
    text-align: center;
    color: var(--brand-blue);
    font-weight: 700;
  }
  .brand-name {
    display: block;
    font-size: 86px;
    line-height: 1;
    letter-spacing: 2px;
  }
  .brand-tagline {
    display: block;
    margin-top: 8px;
    font-size: 22px;
    letter-spacing: 6px;
  }
  .person-name {
    position: absolute;
    left: 118px;
    top: 440px;
    color: var(--text-light);
    font-size: 44px;
    font-weight: 400;
    letter-spacing: 1px;
  }
  .contact-list {
    position: absolute;
    left: 555px;
    top: 335px;
    list-style: none;
    color: var(--text-light);
    font-size: 20px;
  }
  .contact-item {
    display: flex;
    align-items: center;
    gap: 14px;
    height: 32px;
  }
  .contact-icon {
    width: 20px;
    height: 20px;
    fill: var(--text-light);
    flex: none;
  }
</style>
</head>
<body>
<main class="stage">
  <section class="business-card">
    <svg class="card-wave" viewBox="0 0 1000 572" preserveAspectRatio="none" aria-hidden="true">
      <path class="wave-fill" d="M0 110 C 250 240, 700 300, 1000 190 L1000 572 L0 572 Z"/>
      <path class="wave-line" d="M0 110 C 250 240, 700 300, 1000 190"/>
    </svg>

    <div class="brand">
      <span class="brand-name">QOVO</span>
      <span class="brand-tagline">INTERNATIONAL</span>
    </div>

    <h1 class="person-name">DENNIS MARLOW</h1>

    <ul class="contact-list">
      <li class="contact-item">
        <svg class="contact-icon" viewBox="0 0 24 24" aria-hidden="true"><path d="M6.6 10.8a15 15 0 0 0 6.6 6.6l2.2-2.2a1 1 0 0 1 1-.25 11.4 11.4 0 0 0 3.6.57 1 1 0 0 1 1 1V20a1 1 0 0 1-1 1A17 17 0 0 1 3 4a1 1 0 0 1 1-1h3.5a1 1 0 0 1 1 1c0 1.25.2 2.45.57 3.57a1 1 0 0 1-.25 1z"/></svg>
        <span>+61 427581962</span>
      </li>
      <li class="contact-item">
        <svg class="contact-icon" viewBox="0 0 24 24" aria-hidden="true"><path d="M2 5h20v14H2z M4 7v.5l8 5 8-5V7z" fill-rule="evenodd"/></svg>
        <span>dennis@qovo.com.au</span>
      </li>
      <li class="contact-item">
        <svg class="contact-icon" viewBox="0 0 24 24" aria-hidden="true"><path d="M12 2a7 7 0 0 0-7 7c0 5 7 13 7 13s7-8 7-13a7 7 0 0 0-7-7zm0 9.5A2.5 2.5 0 1 1 12 6.5a2.5 2.5 0 0 1 0 5z"/></svg>
        <span>P.O. Box 872 Kelvindale QLD 4309</span>
      </li>
    </ul>
  </section>
</main>
</body>
</html>
```